Calvera fine stockings - sexy cardboard box design needed!

We need a packaging design for a new online company based in Sydney called 'Calvera Hosiery'. We will be selling sexy stockings to our customers by Italian designers. We mainly feature lace stockings, an example of which, can be seen here:
http://www.brindelatessuti.example/italy-FASHION-WINTER

The design should be a cardboard pull out box, black in colour with the logo on the cover. We are looking for the logo to communicate sophistication and sexiness.

Examples of cardboard box shapes we would like are:
http://www.tradovex.example/product-gs/583016294/High_quality_drawer_paper_box.html

http://www.tradovex.example/product-gs/536192047/Cardboard_drawer_box.html

29 December:
I submitted a note when I extended the deadline, but cannot see it, so will write here for clarification. It has been difficult to choose the best design as the designs submitted were of such high quality. I want to have some people judge the designs, but because of the Christmas Season I have extended the deadline so that this can be done. Thanks.

Target Market(s)

The working professional woman.

Industry/Entity Type

Fashion

Requirements
Must have
• The words "Calvera Hosiery" on the cover of the box.

The box should be a sliding drawer.

The box size should be: (22*15*2.5cm).

Washing instructions and recycling logos on the back of the box. See example of uploaded file.

Nice to have
• It would be nice to have the background of the box a dark colour, maybe charcoal? But we are open to all ideas.
Should not have
• A stock photo on cover of box.

```html
<!DOCTYPE html>
<html lang="en">
<head>
<meta charset="utf-8">
<title>Calvera Hosiery – Drawer Box Dieline</title>
<link rel="stylesheet" href="https://fonts.googleapis.com/css2?family=Archivo+Black&display=swap">
<style>
  :root {
    --page: #ffffff;
    --board: #15181d;
    --board-glow: #2b3440;
    --stripe: rgba(0, 0, 0, 0.35);
    --brand-text: #d9d4cc;
    --care-mark: #8a7560;
    --label: #232830;
  }
  * { margin: 0; padding: 0; box-sizing: border-box; }
  html, body { width: 1200px; height: 900px; overflow: hidden; background: var(--page); }
  .canvas { position: relative; width: 1200px; height: 900px; background: var(--page); }

  .panel {
    position: absolute;
    background:
      repeating-linear-gradient(to bottom, transparent 0 5px, var(--stripe) 5px 9px),
      var(--board);
  }
  .panel--lit {
    background:
      repeating-linear-gradient(to bottom, transparent 0 5px, var(--stripe) 5px 9px),
      radial-gradient(ellipse at center, var(--board-glow) 0%, var(--board) 60%);
  }

  /* outer sleeve */
  .outer-back   { left: 93px;  top: 245px; width: 214px; height: 313px; }
  .outer-spine  { left: 310px; top: 245px; width: 35px;  height: 313px; }
  .outer-cover  { left: 348px; top: 245px; width: 215px; height: 313px; }
  .outer-edge   { left: 566px; top: 245px; width: 35px;  height: 313px; }
  .outer-flap-top    { left: 348px; top: 205px; width: 215px; height: 35px; }
  .outer-flap-bottom { left: 348px; top: 562px; width: 215px; height: 35px; }

  .care-symbols {
    position: absolute; left: 50px; top: 145px; width: 122px; height: 14px;
    background: var(--care-mark); opacity: 0.6; border-radius: 2px;
  }

  .brand-name {
    position: absolute; left: 0; top: 146px; width: 100%;
    font-family: "Archivo Black", sans-serif;
    font-weight: 400;
    font-size: 14px; letter-spacing: 1.5px; line-height: 1;
    text-transform: uppercase; text-align: center;
    color: var(--brand-text);
  }

  /* inner drawer */
  .inner-base { left: 782px; top: 245px; width: 213px; height: 313px; }
  .inner-wall-top-outer    { left: 782px; top: 173px; width: 211px; height: 34px; }
  .inner-wall-top-inner    { left: 782px; top: 210px; width: 211px; height: 32px; }
  .inner-wall-bottom-inner { left: 782px; top: 562px; width: 211px; height: 34px; }
  .inner-wall-bottom-outer { left: 782px; top: 599px; width: 211px; height: 32px; }
  .inner-wall-left-outer   { left: 707px; top: 245px; width: 34px; height: 313px; }
  .inner-wall-left-inner   { left: 745px; top: 245px; width: 34px; height: 313px; }
  .inner-wall-right-inner  { left: 998px; top: 245px; width: 33px; height: 313px; }
  .inner-wall-right-outer  { left: 1035px; top: 245px; width: 35px; height: 313px; }

  .part-label {
    position: absolute;
    font-family: "Archivo Black", sans-serif;
    font-size: 28px; line-height: 1; color: var(--label);
    white-space: nowrap; text-align: center;
    transform: scaleX(1.3); transform-origin: center;
  }
  .part-label--outer { left: 352px; top: 670px; width: 200px; }
  .part-label--inner { left: 788px; top: 664px; width: 200px; }
</style>
</head>
<body>
<main class="canvas">
  <section class="dieline dieline--outer" aria-label="Outer sleeve">
    <div class="panel panel--lit outer-back">
      <div class="care-symbols" role="img" aria-label="Washing instructions and recycling symbols"></div>
    </div>
    <div class="panel outer-spine"></div>
    <div class="panel panel--lit outer-cover">
      <h1 class="brand-name">Calvera Hosiery</h1>
    </div>
    <div class="panel outer-edge"></div>
    <div class="panel outer-flap-top"></div>
    <div class="panel outer-flap-bottom"></div>
  </section>

  <section class="dieline dieline--inner" aria-label="Inner drawer">
    <div class="panel panel--lit inner-base"></div>
    <div class="panel inner-wall-top-outer"></div>
    <div class="panel inner-wall-top-inner"></div>
    <div class="panel inner-wall-bottom-inner"></div>
    <div class="panel inner-wall-bottom-outer"></div>
    <div class="panel inner-wall-left-outer"></div>
    <div class="panel inner-wall-left-inner"></div>
    <div class="panel inner-wall-right-inner"></div>
    <div class="panel inner-wall-right-outer"></div>
  </section>

  <p class="part-label part-label--outer">outer box</p>
  <p class="part-label part-label--inner">inner box</p>
</main>
</body>
</html>
```